New Zealand Kestrel Bridgeway Flyer

A 2 sided DL size flyer. (Approx 20cm long by 10cm wide)
That has logo and blurb about company on front. On back details of Kestrel bridgeway package, trademark, contact details and license numbers.
We feel we need to see the text on the flyer design and then make some changes so there will be some back and forth about written content. There may be a reduction in the amount of text we want for the blurb about the company but the rest is mandatory.
Our logo is blue and green, we do not want a white flyer with black text as feel this looks homemade so we need your suggestions about what colour the text and flyer could be.
We want the flyer to look clean and modern. It will go on a stand at an immigration fair and will be sent in the post and via email to clients. We will need posters at a later stage.
Migrants
It Company

```html
<!DOCTYPE html>
<html lang="en">
<head>
<meta charset="utf-8">
<title>New Zealand Kestrel Bridgeway – DL Flyer</title>
<link rel="stylesheet" href="https://fonts.googleapis.com/css2?family=Open+Sans:ital,wght@0,400;0,600;0,700;1,600;1,700&family=Ubuntu:wght@400;500&display=swap">
<style>
:root{
  --blue:#1b5cab;
  --navy:#0e2f6b;
  --navy-deep:#0a2356;
  --green:#3aaa35;
  --green-soft:#9ab36b;
  --text:#4a4a4a;
  --paper:#ffffff;
  --paper-grey:#f2f2f2;
  --lavender:#e3e2f1;
  --backdrop:#e9e7e4;
  --photo-light:#b9c6d4;
  --photo-dark:#8ea3b8;
}
*{box-sizing:border-box;margin:0;padding:0}
html,body{width:1200px;height:1178px;overflow:hidden;background:var(--backdrop)}
body{position:relative;font-family:"Open Sans",Arial,sans-serif;color:var(--text)}
.panel{position:absolute;top:92px;width:472px;height:993px;background:var(--paper);overflow:hidden;box-shadow:0 2px 6px rgba(0,0,0,.15)}
.panel--front{left:108px}
.panel--back{left:620px;background:var(--paper-grey)}
.abs{position:absolute}
.hero-art{position:absolute;left:0;top:0}
.badge{position:absolute;width:88px;height:88px;border-radius:50%;background:var(--green-soft);border:4px solid #d9d9d9}
.brand{position:absolute;display:flex;align-items:center}
.brand__mark{width:80px;height:80px;border-radius:50%;background:var(--green);flex:none}
.brand__rule{width:2px;height:88px;background:#333;margin:0 10px 0 18px}
.brand__name{font-family:"Ubuntu",sans-serif;font-weight:500;color:var(--blue);line-height:1}
.brand__name span{display:block}
.brand__name .l1{font-size:34px}
.brand__name .l2{font-size:26px;margin-top:2px}
.brand__name .l3{font-size:15px;letter-spacing:4px;margin-top:5px}
.headline{font-family:"Ubuntu",sans-serif;color:var(--blue);text-align:center;width:100%;left:0}
.pill{position:absolute;background:var(--green);color:#fff;border-radius:15px;text-align:center;font-family:"Ubuntu",sans-serif}
.copy{position:absolute;left:21px;width:430px;font-size:11.2px;line-height:15px;text-align:justify}
.copy em{font-weight:700}
.quote{position:absolute;left:32px;top:760px;width:408px;height:60px;border:1px dotted var(--green);border-radius:4px;padding:8px 14px 0 40px;font-size:12.5px;line-height:22px}
.quote__mark{position:absolute;left:8px;top:-8px;font-family:Georgia,serif;font-size:48px;font-weight:700;color:var(--green);line-height:1}
.footer{position:absolute;left:0;top:905px;width:472px;height:88px}
.footer__art{position:absolute;left:0;top:0}
.footer__fb{position:absolute;left:23px;top:40px;width:38px;height:38px;border-radius:50%;background:var(--green)}
.footer__info{position:absolute;left:0;width:100%;top:20px;text-align:center;color:#fff;font-size:11px;line-height:17px}
.footer__web{font-weight:700;font-size:16px;letter-spacing:.3px;margin-top:2px}
.bullets{position:absolute;left:20px;top:336px;width:432px;list-style:none;font-size:11px;line-height:15px}
.bullets li{position:relative;padding-left:17px;margin-bottom:10px}
.bullets li::before{content:"";position:absolute;left:0;top:3px;width:9px;height:9px;border-radius:50%;background:var(--green)}
.bullets li::after{content:"";position:absolute;left:2px;top:5.5px;width:3px;height:3px;border-right:1.3px solid #fff;border-top:1.3px solid #fff;transform:rotate(45deg)}
.steps{position:absolute;left:20px;top:543px;width:435px;height:148px;border:1px dotted var(--green);border-radius:6px;display:flex;padding-top:20px;background:var(--paper)}
.step{flex:1;text-align:center;font-size:9.6px;line-height:13.5px;padding:0 14px}
.step--alt{background:var(--lavender);margin-top:-20px;padding-top:20px}
.step__num{font-family:Georgia,serif;font-size:26px;color:var(--blue);line-height:1;margin-bottom:10px}
.contact{position:absolute;left:216px;font-size:15px;line-height:18px;color:#777}
.contact__name{color:var(--blue);display:inline-block;width:70px}
.contact__phone{color:var(--navy)}
.phone-icon{display:inline-block;vertical-align:-2px;margin-right:6px}
</style>
</head>
<body>

<section class="panel panel--front">
  <svg class="hero-art" width="472" height="400" viewBox="0 0 472 400">
    <defs>
      <linearGradient id="heroTone" x1="0" y1="0" x2="0" y2="1">
        <stop offset="0" stop-color="var(--photo-light)"/>
        <stop offset="1" stop-color="var(--photo-dark)"/>
      </linearGradient>
    </defs>
    <path d="M0 0H472V335Q250 400 0 318Z" fill="var(--green)"/>
    <path d="M0 0H472V328Q250 388 0 312Z" fill="url(#heroTone)" role="img" aria-label="Photo: smiling student holding a red folder in front of a snow-capped mountain and lake"/>
  </svg>
  <div class="badge" style="left:368px;top:306px" role="img" aria-label="Licensing authority badge"></div>

  <div class="brand" style="left:61px;top:410px">
    <div class="brand__mark"></div>
    <div class="brand__rule"></div>
    <div class="brand__name"><span class="l1">New Zealand</span><span class="l2">Kestrel Bridgeway</span><span class="l3">Immigration Advice</span></div>
  </div>

  <h2 class="abs headline" style="top:526px;font-size:16.5px;font-weight:400">FRIENDLY &amp; HELPFUL LICENSED IMMIGRATION ADVISERS</h2>
  <div class="pill" style="left:41px;top:562px;width:388px;height:30px;line-height:30px;font-size:14px">WE FACILITATE FAST AND PROBLEM FREE VISAS</div>

  <p class="copy" style="top:616px">New Zealand Kestrel Bridgeway is a family business; headed by two sisters – Nina and Tessa Harlow. Originally from the UK they migrated to New Zealand over ten years ago, so understand how it feels to move to a new country &amp; go through the visa process.</p>
  <p class="copy" style="top:691px">Tessa &amp; Nina are passionate about what New Zealand has to offer and enjoy the chance to help people make their home here. They work across all types of visa applications – <em><i>to live, work or study.</i></em></p>

  <div class="quote"><span class="quote__mark">“</span>Working closely with you to meet your immigration goals, we help and guide you at every stage.”</div>

  <p class="copy" style="top:848px">Trained and qualified, they have specialist knowledge of the immigration system. Able to work to urgent timeframes or with clients who have character or health issues.</p>

  <footer class="footer">
    <svg class="footer__art" width="472" height="88" viewBox="0 0 472 88">
      <defs><linearGradient id="navyBand" x1="0" y1="0" x2="0" y2="1"><stop offset="0" stop-color="var(--navy)"/><stop offset="1" stop-color="var(--navy-deep)"/></linearGradient></defs>
      <path d="M0 8Q236 -10 472 14V88H0Z" fill="var(--green)"/>
      <path d="M0 18Q236 2 472 24V88H0Z" fill="url(#navyBand)"/>
    </svg>
    <div class="footer__fb"></div>
    <div class="footer__info">
      <div>021 555 0148 &nbsp;| 021 555 0192</div>
      <div>hello@nzkestrelbridgeway.nz</div>
      <div class="footer__web">www.nzkestrelbridgeway.nz</div>
    </div>
  </footer>
</section>

<section class="panel panel--back">
  <svg class="hero-art" width="472" height="185" viewBox="0 0 472 185">
    <path d="M0 0H472V116Q250 232 0 128Z" fill="var(--blue)"/>
    <path d="M0 0H472V108Q250 222 0 120Z" fill="var(--green)"/>
    <path d="M0 0H472V100Q250 212 0 112Z" fill="var(--paper)"/>
  </svg>
  <div class="brand" style="left:61px;top:38px">
    <div class="brand__mark"></div>
    <div class="brand__rule"></div>
    <div class="brand__name"><span class="l1">New Zealand</span><span class="l2">Kestrel Bridgeway</span><span class="l3">Immigration Advice</span></div>
  </div>

  <h2 class="abs headline" style="top:198px;font-size:19px;font-weight:500">KESTREL BRIDGEWAY PACKAGE</h2>
  <p class="copy" style="top:232px;left:20px;width:432px">Set yourself on a clear pathway from your first student visa to permanent residency with our comprehensive immigration package.</p>
  <p class="copy" style="top:277px;left:20px;width:432px">Connect with licensed advisers who walk alongside you in your New Zealand journey, helping to make the most of your time and money</p>

  <ul class="bullets">
    <li>Confirmed, discounted rates for ongoing visas once your study is completed</li>
    <li>A one on one session with a licensed adviser to plan how to maximise your studies &amp; work opportunities to achieve residency faster</li>
    <li>Attendance at an immigration seminar</li>
    <li>Vital updates on immigration policy changes &amp; how they impact on you</li>
    <li>Access immediate advice from someone who knows your situation if things go wrong</li>
  </ul>

  <div class="steps">
    <div class="step"><div class="step__num">1</div>Deposit of 15% which covers Post Study Open Visa (job search)</div>
    <div class="step step--alt"><div class="step__num">2</div>Either Post Study Employer Assisted Visa or Essential Skills Work Visa (this includes employer support)</div>
    <div class="step"><div class="step__num">3</div>Either Skilled Migrant Category Residence or Work to Residence Visa (both components for latter)</div>
  </div>
  <div class="pill" style="left:37px;top:525px;width:398px;height:30px;line-height:30px;font-size:12.5px">Our Kestrel Bridgeway Package includes 3 visa applications</div>

  <p class="abs" style="top:727px;width:100%;text-align:center;font-size:12.5px">Add on’s for family and work options available.</p>
  <p class="abs" style="top:755px;width:100%;text-align:center;font-size:12.5px;font-weight:700;font-style:italic;color:var(--green)">Let New Zealand Kestrel Bridgeway plan your route to residency.</p>

  <div class="badge" style="left:86px;top:796px" role="img" aria-label="Licensing authority badge"></div>

  <div class="contact" style="top:799px">
    <div><span class="contact__name">Tessa</span><span class="contact__phone"><svg class="phone-icon" width="14" height="14" viewBox="0 0 14 14"><circle cx="7" cy="7" r="7" fill="var(--blue)"/><path d="M4.5 3.6l1.4-.3.7 1.8-.9.7q.7 1.5 2.1 2.2l.7-.9 1.8.7-.3 1.4Q6.5 9.4 4.5 3.6z" fill="#fff"/></svg>021 555 0148</span></div>
    <div>License Number 209900417</div>
  </div>
  <div class="contact" style="top:844px">
    <div><span class="contact__name">Nina</span><span class="contact__phone"><svg class="phone-icon" width="14" height="14" viewBox="0 0 14 14"><circle cx="7" cy="7" r="7" fill="var(--blue)"/><path d="M4.5 3.6l1.4-.3.7 1.8-.9.7q.7 1.5 2.1 2.2l.7-.9 1.8.7-.3 1.4Q6.5 9.4 4.5 3.6z" fill="#fff"/></svg>021 555 0192</span></div>
    <div>License Number 209900583</div>
  </div>

  <footer class="footer">
    <svg class="footer__art" width="472" height="88" viewBox="0 0 472 88">
      <defs><linearGradient id="navyBand2" x1="0" y1="0" x2="0" y2="1"><stop offset="0" stop-color="var(--navy)"/><stop offset="1" stop-color="var(--navy-deep)"/></linearGradient></defs>
      <path d="M0 8Q236 -10 472 14V88H0Z" fill="var(--green)"/>
      <path d="M0 18Q236 2 472 24V88H0Z" fill="url(#navyBand2)"/>
    </svg>
    <div class="footer__fb"></div>
    <div class="footer__info">
      <div>021 555 0148 &nbsp;| 021 555 0192</div>
      <div>hello@nzkestrelbridgeway.nz</div>
      <div class="footer__web">www.nzkestrelbridgeway.nz</div>
    </div>
  </footer>
</section>

</body>
</html>
```